book cover self-publishing dystopia autism

I'm looking for an attractive cover to increase sales of my self-published book.
The book is a dystopia science fiction that addresses the subject of autism.
The title is Vorna. The name of the author is Ingrid FALLOW. which must appear on the first cover
Expected: 1st cover, 1st cover and 4th cover, for paper and ebook version

The story takes place on earth, not in space. A software manages the daily lives of people, it could be illustrated or not. Two communities are opposed. The book is written in the first person singular, which is the heroine of an 18-year-old woman. The story takes place in Europe, in a rural universe architecture metal glass, with a futuristic metro

The synopsis: Odette is part of the Elite. She will soon reach her 13th Rainbow, she hopes to be part of the Vorna Leaders. She wants to know if anyone can take her place for the next six months. She's going to do everything she can to find out, but she's also going to find out more and question her certainties about Vorna. His contacts with the Inferior gradually broke down the barriers separating them. However, it is social contacts that have defined the distinction between Elite and Inferior. In the past, the members of the Elite were a stigmatized minority, the autistic and the Inferior the norm, the neurotypical. And if Odette's perfect world was not just, should it be preserved or destroyed?

Target Market(s)

The book is aimed at a young adult or adolescent audience

Requirements
Must have
• An ISBN barcode will be placed in a 50.8 mm (2 in.) X 30.5 mm (1.2 in.) White frame in the lower right corner of the back cover.

Cover page size 1 and 4: 12.7 x 20.32cm
Template for the attached cover

Include the price of the book in 4th cover: 9.95 € TTC

Include on the 1st and 4th cover the author's name "Ingrid Fallow" and the title "Vorna"

Synopsis in 4th cover in French:

Odétte is part of the Elite. She will soon reach her 13th Rainbow, so she hopes to be part of Vorna's Leaders. She wants at all costs to know if someone can take her place during the next 6 months. She will do everything to find out, but she will also discover much more and question her certainties about Vorna. His contacts with the Inferior gradually break down the barriers that separate them. Yet it is the social contacts that defined the distinction between Elite and Inferior. In the past, the Elite were a stigmatized minority, the autistic and the Inferior the norm, the neurotypical. And if Odette's perfect world wasn't fair, should it be preserved or destroyed?

```html
<!DOCTYPE html>
<html lang="en">
<head>
<meta charset="utf-8">
<title>Vorna – Ingrid Fallow – Cover</title>
<link rel="stylesheet" href="https://fonts.googleapis.com/css2?family=Oswald:wght@300;400&family=Source+Sans+3:wght@400&display=swap">
<style>
  :root {
    --sheet: #000000;
    --paper: #ffffff;
    --ink-blue: #2a2a9e;
    --ink-violet: #3a1670;
    --ink-teal: #5fb8c4;
    --ink-royal: #3b3fc0;
    --spine-red: #8a0f2a;
    --spine-plum: #4a1a6a;
    --art-violet: #4b2fa8;
    --art-blue: #2f46c8;
    --art-cyan: #56c6d6;
    --art-red: #8e1830;
    --frame: #333333;
  }
  * { box-sizing: border-box; margin: 0; padding: 0; }
  html, body { width: 897px; height: 1200px; overflow: hidden; background: var(--sheet); }
  .sheet { position: relative; width: 897px; height: 1200px; background: var(--sheet); }

  .panel { position: absolute; background: var(--paper); overflow: hidden; }
  .panel--spread { left: 111px; top: 71px; width: 676px; height: 495px; }
  .panel--front { left: 111px; top: 586px; width: 680px; height: 544px; }

  .display { font-family: "Oswald", "Arial Narrow", sans-serif; font-weight: 400; letter-spacing: 0.02em; white-space: nowrap; }
  .title-ink {
    background: linear-gradient(90deg, var(--ink-violet) 0%, var(--ink-royal) 45%, var(--ink-teal) 100%);
    -webkit-background-clip: text; background-clip: text; color: transparent;
  }

  /* back cover */
  .back-title { position: absolute; left: 0; width: 324px; top: 36px; text-align: center; font-size: 44px; line-height: 1; }
  .back-subtitle { position: absolute; left: 0; width: 324px; top: 86px; text-align: center; font-size: 12px; color: var(--ink-blue); font-weight: 300; }
  .synopsis {
    position: absolute; left: 36px; top: 114px; width: 255px; z-index: 2;
    font-family: "Source Sans 3", "Myriad Pro", sans-serif; font-size: 9.6px; line-height: 12.5px;
    color: var(--ink-blue); text-align: justify;
  }
  .puzzle-small {
    position: absolute; left: 142px; top: 306px; width: 38px; height: 38px;
    background: radial-gradient(circle at 40% 40%, var(--art-violet), var(--art-blue) 70%, var(--art-cyan));
    border-radius: 6px; transform: rotate(20deg);
  }
  .isbn-frame { position: absolute; left: 172px; top: 401px; width: 121px; height: 73px; background: var(--paper); border: 1px solid var(--frame); z-index: 3; }
  .price { position: absolute; left: 37px; top: 462px; font-family: "Source Sans 3", sans-serif; font-size: 9.5px; color: var(--ink-blue); }

  .portrait-back {
    position: absolute; left: 236px; top: 40px; width: 131px; height: 455px;
    background: linear-gradient(90deg, rgba(255,255,255,0) 0%, rgba(220,170,200,0.35) 50%, var(--art-red) 100%);
    border-top-left-radius: 80px 120px;
  }

  /* spine */
  .spine {
    position: absolute; left: 308px; top: 0; width: 59px; height: 495px; z-index: 2;
    background: linear-gradient(180deg, var(--spine-red) 0%, var(--spine-plum) 60%, var(--art-violet) 100%);
  }
  .spine-text {
    position: absolute; left: 50%; top: 50%;
    transform: translate(-50%, -50%) rotate(90deg);
    color: var(--paper); line-height: 1; display: flex; align-items: baseline; gap: 26px;
  }
  .spine-text .spine-author { font-size: 34px; font-weight: 300; }
  .spine-text .spine-title { font-size: 44px; }

  /* front cover */
  .front-cover { position: absolute; width: 309px; height: 495px; background: var(--paper); overflow: hidden; }
  .panel--spread .front-cover { left: 367px; top: 0; }
  .panel--front .front-cover { left: 201px; top: 50px; transform: scale(0.9); transform-origin: top left; box-shadow: 0 0 0 1px #eeeeee; }

  .portrait-front {
    position: absolute; left: 0; top: 40px; width: 128px; height: 455px;
    background: linear-gradient(160deg, var(--art-violet) 0%, var(--art-blue) 45%, var(--art-cyan) 62%, var(--art-blue) 80%, var(--art-violet) 100%);
    border-top-right-radius: 70px 110px;
  }
  .author-first { position: absolute; right: 17px; top: 36px; font-size: 25px; line-height: 1; color: var(--ink-royal); font-weight: 300; }
  .author-last { position: absolute; right: 17px; top: 64px; font-size: 36px; line-height: 1; color: var(--ink-violet); }
  .front-title { position: absolute; right: 14px; top: 170px; font-size: 56px; line-height: 1; }
  .front-subtitle { position: absolute; right: 12px; top: 236px; font-size: 15px; line-height: 1; color: var(--ink-blue); font-weight: 300; }
  .puzzle-large {
    position: absolute; left: 160px; top: 290px; width: 122px; height: 122px;
    background: radial-gradient(circle at 40% 40%, var(--art-violet), var(--ink-violet) 55%, var(--art-blue));
    border-radius: 14px; transform: rotate(20deg);
  }
  .city-band {
    position: absolute; left: 128px; top: 430px; width: 181px; height: 65px;
    background: linear-gradient(180deg, rgba(75,47,168,0) 0%, rgba(75,47,168,0.75) 40%, var(--art-blue) 100%);
  }
</style>
</head>
<body>
<div class="sheet">

  <section class="panel panel--spread">
    <div class="back-cover">
      <h2 class="back-title display title-ink">VORNA</h2>
      <p class="back-subtitle display">L'UNIVERS DE L'AUTISME</p>
      <div class="portrait-back" role="img" aria-label="Painted young woman's hair and shoulder fading into white"></div>
      <p class="synopsis">Odétte is part of the Elite. She will soon reach her 13th Rainbow, so she hopes to be part of Vorna's Leaders. She wants at all costs to know if someone can take her place during the next 6 months. She will do everything to find out, but she will also discover much more and question her certainties about Vorna. His contacts with the Inferior gradually break down the barriers that separate them. Yet it is the social contacts that defined the distinction between Elite and Inferior. In the past, the Elite were a stigmatized minority, the autistic and the Inferior the norm, the neurotypical. And if Odette's perfect world wasn't fair, should it be preserved or destroyed?</p>
      <div class="puzzle-small" role="img" aria-label="Small painted jigsaw puzzle piece"></div>
      <div class="isbn-frame"></div>
      <p class="price">€ 9.95 TTC</p>
    </div>

    <div class="spine">
      <div class="spine-text display">
        <span class="spine-author">INGRID FALLOW</span>
        <span class="spine-title">VORNA</span>
      </div>
    </div>

    <div class="front-cover">
      <div class="portrait-front" role="img" aria-label="Painted portrait of a young woman looking down over her shoulder in violet, blue and cyan"></div>
      <p class="author-first display">INGRID</p>
      <p class="author-last display">FALLOW</p>
      <h1 class="front-title display title-ink">VORNA</h1>
      <p class="front-subtitle display">L'UNIVERS DE L'AUTISME</p>
      <div class="puzzle-large" role="img" aria-label="Large textured jigsaw puzzle piece"></div>
      <div class="city-band" role="img" aria-label="Blue city skyline illustration"></div>
    </div>
  </section>

  <section class="panel panel--front">
    <div class="front-cover">
      <div class="portrait-front" role="img" aria-label="Painted portrait of a young woman looking down over her shoulder in violet, blue and cyan"></div>
      <p class="author-first display">INGRID</p>
      <p class="author-last display">FALLOW</p>
      <h1 class="front-title display title-ink">VORNA</h1>
      <p class="front-subtitle display">L'UNIVERS DE L'AUTISME</p>
      <div class="puzzle-large" role="img" aria-label="Large textured jigsaw puzzle piece"></div>
      <div class="city-band" role="img" aria-label="Blue city skyline illustration"></div>
    </div>
  </section>

</div>
</body>
</html>
```